Sale- Bundle signs

We are looking for a design to use for Permanent SALE/Bundle deal signs. We are a natural bath products company who uses all natural ingredients to create our handmade line of natural products. We love a clean, fresh look and feel. Simple eye-catching that will be a quick glance and they will know the offer.
We would like to have something simple, eye catching that will promote sales on our different products.
Dead Sea Salt Body Scrubs
large 2 for $40
small 3 for $20
Moisturizing Wash with coconut & olive oil
2 for $20
There are several more needed but we are hoping to decide on one template before making all of the signs.
Visit our website here www.brightwillowco.com
Target Market(s)
Our store serves 70% women and the majority of our customers are 30+ years old.
Industry/Entity Type
It Company
Other font styles liked:
- Century Gothic or similar
Look and feel

```html
<!DOCTYPE html>
<html lang="en">
<head>
<meta charset="UTF-8">
<title>Bright Willow – Sales/Promotion Sign</title>
<link rel="stylesheet" href="https://fonts.googleapis.com/css2?family=Montserrat:ital,wght@0,500;0,600;0,700;1,500&display=swap">
<style>
  :root {
    --leaf: #5f9e1c;
    --leaf-bright: #7fbf2a;
    --leaf-pale: #eef6e0;
    --orange: #f47b20;
    --paper: #ffffff;
    --ink-light: #ffffff;
  }
  * { margin: 0; padding: 0; box-sizing: border-box; }
  html, body { width: 857px; height: 1200px; overflow: hidden; background: var(--paper); }
  .sign {
    position: relative;
    width: 857px;
    height: 1200px;
    background: var(--paper);
    font-family: "Montserrat", "Century Gothic", sans-serif;
    text-align: center;
  }
  .swirl-backdrop {
    position: absolute;
    inset: 24px;
    background: radial-gradient(ellipse at 50% 55%, var(--paper) 0%, var(--leaf-pale) 100%);
  }
  .wave-frame { position: absolute; inset: 0; }

  .brand {
    position: absolute;
    top: 78px;
    left: 0; right: 0;
  }
  .brand-name {
    display: inline-flex;
    align-items: center;
    gap: 18px;
    font-size: 60px;
    font-weight: 700;
    line-height: 1;
    letter-spacing: 4px;
    color: var(--leaf);
  }
  .brand-dot {
    width: 16px;
    height: 16px;
    border-radius: 50%;
    background: var(--orange);
  }
  .brand-tagline {
    margin-top: 22px;
    font-size: 20px;
    font-weight: 600;
    letter-spacing: 7px;
    color: var(--leaf-bright);
  }

  .headline {
    position: absolute;
    top: 272px;
    left: 0; right: 0;
    font-size: 48px;
    font-weight: 700;
    color: var(--orange);
    letter-spacing: 0.5px;
  }
  .headline-rule { position: absolute; top: 335px; left: 351px; }

  .offer {
    position: absolute;
    left: 180px;
    width: 497px;
    color: var(--ink-light);
  }
  .offer-shape { position: absolute; inset: 0; }
  .offer-body { position: relative; }
  .offer-title { font-size: 26px; font-weight: 700; letter-spacing: 0.3px; }
  .offer-note { font-size: 22px; font-style: italic; font-weight: 500; margin-top: 4px; }
  .offer-line { font-size: 26px; font-weight: 500; margin-top: 12px; }
  .offer-line .price { font-size: 42px; font-weight: 700; }

  .offer--scrubs { top: 386px; height: 280px; }
  .offer--scrubs .offer-body { padding-top: 60px; }
  .offer--wash { top: 703px; height: 250px; }
  .offer--wash .offer-body { padding-top: 52px; }

  .contact {
    position: absolute;
    top: 1012px;
    left: 0; right: 0;
    color: var(--leaf);
    font-weight: 700;
  }
  .contact-web { font-size: 34px; }
  .contact-phone { font-size: 39px; margin-top: 8px; }
</style>
</head>
<body>
<main class="sign">
  <div class="swirl-backdrop" role="img" aria-label="Faint pale green floral swirl pattern"></div>

  <svg class="wave-frame" width="857" height="1200" viewBox="0 0 857 1200" aria-hidden="true">
    <defs>
      <pattern id="wave-h" width="12" height="8" patternUnits="userSpaceOnUse">
        <path d="M0 4 Q3 0 6 4 T12 4" fill="none" stroke="#7fbf2a" stroke-width="1.6"/>
      </pattern>
      <pattern id="wave-v" width="12" height="8" patternUnits="userSpaceOnUse" patternTransform="rotate(90)">
        <path d="M0 4 Q3 0 6 4 T12 4" fill="none" stroke="#7fbf2a" stroke-width="1.6"/>
      </pattern>
    </defs>
    <rect x="14" y="12" width="829" height="8" fill="url(#wave-h)"/>
    <rect x="14" y="1180" width="829" height="8" fill="url(#wave-h)"/>
    <rect x="12" y="14" width="8" height="1172" fill="url(#wave-v)"/>
    <rect x="837" y="14" width="8" height="1172" fill="url(#wave-v)"/>
  </svg>

  <header class="brand">
    <div class="brand-name"><span class="brand-dot"></span>BRIGHT WILLOW</div>
    <div class="brand-tagline">NATURAL BATH PRODUCTS</div>
  </header>

  <h1 class="headline">SALES/PROMOTION</h1>
  <svg class="headline-rule" width="155" height="14" viewBox="0 0 155 14" aria-hidden="true">
    <path d="M2 7 Q8 1 14 7 T26 7 T38 7 T50 7 T62 7 T74 7 T86 7 T98 7 T110 7 T122 7 T134 7 T146 7 T153 7" fill="none" stroke="#5f9e1c" stroke-width="2"/>
  </svg>

  <section class="offer offer--scrubs">
    <svg class="offer-shape" width="497" height="280" viewBox="0 0 497 280" preserveAspectRatio="none" aria-hidden="true">
      <path d="M30 14 Q70 -4 110 22 Q180 30 248 8 Q316 30 387 22 Q427 -4 467 14 Q480 50 470 70 Q497 140 470 210 Q480 230 467 266 Q427 284 387 258 Q316 250 248 272 Q180 250 110 258 Q70 284 30 266 Q17 230 27 210 Q0 140 27 70 Q17 50 30 14 Z" fill="#5f9e1c"/>
    </svg>
    <div class="offer-body">
      <h2 class="offer-title">DEAD SEA SALT BODY SCRUBS</h2>
      <p class="offer-line">large 2 for <span class="price">$40</span></p>
      <p class="offer-line">small 3 for <span class="price">$20</span></p>
    </div>
  </section>

  <section class="offer offer--wash">
    <svg class="offer-shape" width="497" height="250" viewBox="0 0 497 280" preserveAspectRatio="none" aria-hidden="true">
      <path d="M30 14 Q70 -4 110 22 Q180 30 248 8 Q316 30 387 22 Q427 -4 467 14 Q480 50 470 70 Q497 140 470 210 Q480 230 467 266 Q427 284 387 258 Q316 250 248 272 Q180 250 110 258 Q70 284 30 266 Q17 230 27 210 Q0 140 27 70 Q17 50 30 14 Z" fill="#5f9e1c"/>
    </svg>
    <div class="offer-body">
      <h2 class="offer-title">MOISTURIZING WASH</h2>
      <p class="offer-note">with coconut &amp; olive oil</p>
      <p class="offer-line">2 for <span class="price">$20</span></p>
    </div>
  </section>

  <footer class="contact">
    <div class="contact-web">www.brightwillowco.com</div>
    <div class="contact-phone">555.014.2780</div>
  </footer>
</main>
</body>
</html>
```